Web Site Face Lift - ONLY 2 PAGES

(NOTE: reduced scope)

We are looking for a facelift for www.brightledgerco.com, to make it look more professional and polished.

We need a homepage & a second level page design, to be delivered as layered PhotoShop files.  

Overall, we"re happy with the sky motif. But the look and feel is too home-made.

1. We need a re-designed homepage:www.brightledgerco.com 

2. Workshop details page:http://brightledgerco.com/v7v_details.html

We"re looking for something conceptually creative, that takes into account the idea that "smart businesses profit fromsustainability."  

Here are a couple examples of something we consider conceptually creative, yet fairly simple.  (The content is entirely unrelated to ours: http://www.quorvabent.com/      also        http://plinketrow.com/ )

Regarding the workshop details page (http://brightledgerco.com/v7v_details.html ), we can collect images and quotes(such as the gym owner who appears on the details page near the bottom), which could be turned into a slide show.  In other words, the mockup could have a place for a slide show & use the gym owner content as place holder. 

The logo color needs to stay the same; but you may use any palette you like for the pages, that compliments the color.  We think the white looks clean, but you"re welcome to trysomething else if you want.  

We like the use of photographic images.  
Updates

Thank you very much for the hard work and design suggestions.  We went with the mockup that most polished version, which reflected our vision and clear usability.

Target Market(s)

Target Audiences

FOR THE "SPARK TO LEDGER" WORKSHOP:

Entrepreneurs who have a business idea, but need (legal, financial and business development) advice on how to launch it and/or a push to actually get it started. Specifically:

1. Recent sustainability MBA grads
2. Other MBA grads
3. Those seeking to develop safety net, new idea, or realize dream
- New entrepreneurs
- Job Seekers
- People Currently Employed
- Stay At Home Parents
- Artists, etc.

FOR THE MAIN (BRIGHT-LEDGERCO) SITE

1. CEOs, CFOs, COOs, investor relations officers and/or sustainability advocates who want to increase profit and cut expenses by reducing their environmental footprint.
2. CEOs, CFOs, COOs, investor relations officers and/or sustainability advocates who care about future generations and the environment.

Industry/Entity Type

Consulting

Number of Pages Required

4 pages

Requirements
Must have
• We"d like the pages to feel clean, fresh, alive, inviting. They must exude competence and be unquestionably professional.

The "Spark to Ledger" workshop landing page and secondary page should be exciting, about launching one"s dreams.

The BrightLedgerco homepage concept should convey a message about smart businesses use sustainability to ensure their long-term success.
Nice to have
• THIS IS A NICE TO HAVE FOR THE WINNING DESIGNER:

We wish we could offer a much higher design award for this, but we"re just getting started. To incentivize you, and say thanks for the fantastic job the winning designer does, we will promote your design/development work to our workshop clients. They are new entrepreneurs who we will be advising, among other things, on how to get their web sites set up for their new businesses.

In regards to the last point,

- We will see approximately 20 entrepreneurs at each of our workshops; many will need their own Web sites built. If you"d like, we will show some of your sites in our presentation, and recommend your work based on our redesign/rebuild experience with you.

Should not have
• The pages should NOT feel granola, hippy or tree-hugger.Nor should they look gimmicky, get-rich-quick, cheap or sloppy.

Neither should be cluttered or tacky.

THANK YOU!

```html
<!DOCTYPE html>
<html lang="en">
<head>
<meta charset="utf-8">
<title>BrightLedgerco — Take your business to the next level</title>
<link rel="stylesheet" href="https://fonts.googleapis.com/css2?family=Cabin:wght@400;500;700&family=Arimo:wght@400&display=swap">
<style>
  :root {
    --page-bg: #ececec;
    --card-bg: #ffffff;
    --hero-tint: #eef8ec;
    --green: #1b9a2b;
    --green-dark: #137a1f;
    --blue: #1a9ad6;
    --text-dark: #222222;
    --text-mid: #555555;
    --text-soft: #6a6a6a;
    --rule: #bdbdbd;
    --footer-text: #555555;
  }
  * { box-sizing: border-box; margin: 0; padding: 0; }
  html, body { width: 1200px; height: 1145px; overflow: hidden; }
  body { background: var(--page-bg); font-family: "Cabin", sans-serif; color: var(--text-dark); position: relative; }

  .site-card {
    position: absolute; left: 25px; top: 40px; width: 1140px; height: 1010px;
    background: linear-gradient(180deg, var(--hero-tint) 0, #fbfdfb 260px, var(--card-bg) 420px);
    border-radius: 8px;
    box-shadow: 0 2px 6px rgba(0,0,0,0.12);
  }

  .brand { position: absolute; left: 73px; top: 82px; display: flex; align-items: center; gap: 10px; }
  .brand-dot { width: 30px; height: 30px; border-radius: 50%; background: var(--green); }
  .brand-name { font-size: 24px; font-weight: 500; color: var(--green); }

  .main-nav { position: absolute; top: 108px; left: 360px; display: flex; font-size: 22px; color: var(--text-mid); }
  .main-nav a { position: absolute; white-space: nowrap; color: inherit; text-decoration: none; display: flex; align-items: center; gap: 10px; }
  .main-nav a.is-current { color: var(--green); }
  .main-nav svg { width: 10px; height: 16px; }

  .hero-photo {
    position: absolute; left: 651px; top: 163px; width: 514px; height: 413px;
    background: radial-gradient(ellipse at 55% 45%, #d9cfc2 0, #ece6de 40%, rgba(255,255,255,0) 72%);
  }
  .hero-title { position: absolute; left: 81px; top: 218px; font-size: 70px; font-weight: 700; color: var(--green); letter-spacing: 0.5px; line-height: 1; }
  .hero-subtitle { position: absolute; left: 87px; top: 294px; font-size: 44px; font-weight: 400; color: var(--green); line-height: 1; }
  .hero-lead { position: absolute; left: 90px; top: 358px; font-size: 36px; color: var(--text-soft); line-height: 1; }
  .hero-copy { position: absolute; left: 96px; top: 424px; width: 570px; font-size: 16px; line-height: 22.5px; color: var(--text-dark); }
  .hero-copy p + p { margin-top: 22px; }
  .hero-shadow { position: absolute; left: 207px; top: 571px; width: 764px; height: 10px; background: radial-gradient(ellipse at 50% 0, rgba(0,0,0,0.14), rgba(0,0,0,0) 70%); }

  .benefits { position: absolute; left: 83px; top: 621px; width: 320px; }
  .benefits-intro { font-size: 15.5px; line-height: 22px; color: var(--text-dark); }
  .body-copy { font-family: "Arimo", sans-serif; font-size: 14.5px; line-height: 22.5px; color: var(--text-mid); }
  .benefits .body-copy { margin: 20px 0 0 4px; width: 310px; }
  .benefit-list { list-style: none; margin-top: 18px; }
  .benefit-list li { position: relative; padding-left: 35px; font-family: "Arimo", sans-serif; font-size: 14.5px; line-height: 18px; color: var(--text-dark); height: 52px; }
  .benefit-list svg { position: absolute; left: 3px; top: 2px; width: 16px; height: 16px; }

  .column-divider { position: absolute; left: 440px; top: 623px; height: 317px; border-left: 1px dotted var(--rule); }

  .feature { position: absolute; left: 471px; top: 620px; width: 654px; }
  .feature-title { font-size: 20px; font-weight: 500; color: var(--text-dark); }
  .feature .body-copy { margin-top: 15px; width: 640px; }
  .read-more { display: inline-block; margin-top: 12px; font-family: "Arimo", sans-serif; font-size: 14px; color: var(--blue); text-decoration: underline; }
  .feature-rule { margin-top: 22px; border-top: 1px dotted var(--rule); }
  .workshop-title { margin-top: 18px; font-size: 20px; font-weight: 400; color: var(--blue); }
  .workshop-copy { margin-top: 12px; font-size: 15.5px; line-height: 22px; color: var(--text-dark); }
  .cta-button {
    display: inline-block; margin-top: 18px; width: 268px; height: 41px; line-height: 41px; padding-left: 28px;
    background: linear-gradient(180deg, #2db53a, var(--green-dark));
    border: 1px solid #0e5c17; border-radius: 2px;
    color: #fff; font-size: 18px; font-weight: 700; letter-spacing: 0.3px; text-decoration: none;
  }

  .copyright { position: absolute; left: 50px; top: 1078px; font-family: "Arimo", sans-serif; font-size: 14px; color: var(--footer-text); }
  .contact-block { position: absolute; right: 57px; top: 1065px; text-align: right; font-size: 17px; font-weight: 700; color: #6a6a6a; line-height: 22px; letter-spacing: 0.5px; }
</style>
</head>
<body>
  <main class="site-card">
    <div class="brand">
      <span class="brand-dot"></span>
      <span class="brand-name">BrightLedgerco</span>
    </div>

    <nav class="main-nav">
      <a class="is-current" href="#" style="left:3px"><svg viewBox="0 0 10 16"><path d="M8 2 2 8l6 6" fill="none" stroke="#666" stroke-width="2.4"/></svg>Home</a>
      <a href="#" style="left:111px"><svg viewBox="0 0 10 16"><path d="M8 2 2 8l6 6" fill="none" stroke="#666" stroke-width="2.4"/></svg>Tools &amp; Training</a>
      <a href="#" style="left:311px"><svg viewBox="0 0 10 16"><path d="M8 2 2 8l6 6" fill="none" stroke="#666" stroke-width="2.4"/></svg>Forward Thinking</a>
      <a href="#" style="left:523px"><svg viewBox="0 0 10 16"><path d="M8 2 2 8l6 6" fill="none" stroke="#666" stroke-width="2.4"/></svg>Blog</a>
      <a href="#" style="left:607px"><svg viewBox="0 0 10 16"><path d="M8 2 2 8l6 6" fill="none" stroke="#666" stroke-width="2.4"/></svg>Contact Us</a>
    </nav>

    <div class="hero-photo" role="img" aria-label="Photo of a smiling businessman in a white shirt and striped tie in a bright office"></div>
  </main>

  <h1 class="hero-title">TAKE YOUR BUSINESS</h1>
  <p class="hero-subtitle">TO THE NEXT LEVEL.</p>
  <h2 class="hero-lead">Take your business to the next level.</h2>
  <div class="hero-copy">
    <p>Smart entrepreneurs avoid costly mistakes and get their startups running fast with our launch workshop and platform, Spark to Ledger.</p>
    <p>Companies and nonprofits align their values with their practice when they BrightLedgerco.</p>
  </div>
  <div class="hero-shadow"></div>

  <section class="benefits">
    <p class="benefits-intro">Start profiting today from Bright’s consulting Tools &amp; Training and:</p>
    <p class="body-copy">Praesent gravida sollicitudin mi, vitae iaculis mauris mollis id. In vitae placerat tortor. Nunc id ipsum in dui ornare egestas tempus rhoncus nunc.</p>
    <ul class="benefit-list">
      <li><svg viewBox="0 0 16 16"><circle cx="8" cy="8" r="7" fill="#eee" stroke="#aaa"/><path d="M6.5 5 10 8l-3.5 3z" fill="#777"/></svg>Decrease carbon emissions and waste.</li>
      <li><svg viewBox="0 0 16 16"><circle cx="8" cy="8" r="7" fill="#eee" stroke="#aaa"/><path d="M6.5 5 10 8l-3.5 3z" fill="#777"/></svg>Improve energy, water and materials efficiency.</li>
      <li><svg viewBox="0 0 16 16"><circle cx="8" cy="8" r="7" fill="#eee" stroke="#aaa"/><path d="M6.5 5 10 8l-3.5 3z" fill="#777"/></svg>Generate new revenue streams with sustainability.</li>
    </ul>
  </section>

  <div class="column-divider"></div>

  <section class="feature">
    <h3 class="feature-title">Achieve market advantage. BrightLedgerco today.</h3>
    <p class="body-copy">Praesent gravida sollicitudin mi, vitae iaculis mauris mollis id. In vitae placerat tortor. Nunc id ipsum in dui ornare egestas tempus rhoncus nunc.</p>
    <a class="read-more" href="#">Read More</a>
    <div class="feature-rule"></div>
    <h3 class="workshop-title">Spark to Ledger</h3>
    <p class="workshop-copy">Business launching workshop for entrepreneurs who want to keep start up costs to a minimum</p>
    <a class="cta-button" href="#">GET INFO &amp; REGISTER</a>
  </section>

  <footer>
    <p class="copyright">Copyright 2010 BrightLedgerco.com</p>
    <p class="contact-block">CALL US : 412.555.0186<br>SAN FRANCISCO CA</p>
  </footer>
</body>
</html>
```